Business card design for new brand

We have recently rebranded and need a new business card template.

We are an insurance underwriting agency. All of our products are sold via other partner companies, so these are just to pass on our details to other organisations.

We would like to see designs that use the colour green (current stationary generally uses lime green (rgb 142,190,63) and forest green (0,154,79) to comply with our logo's colours. We are happy with other shades of green.

Business cards need to include our logo, as well as space for:
1. Full name
2. Qualifications (optional)
3. Title
4. Office number
5. Mobile number
6. Email address

Our logo is enclosed here.

```html
<!DOCTYPE html>
<html lang="en">
<head>
<meta charset="utf-8">
<title>Verdant Cover – Business Card</title>
<link rel="stylesheet" href="https://fonts.googleapis.com/css2?family=Poppins:ital,wght@0,400;0,500;0,600;0,700;1,400&display=swap">
<style>
  :root {
    --page-bg: #1a1a1a;
    --card-bg: #ffffff;
    --ink: #111111;
    --forest: #0a9650;
    --forest-dark: #0f6b3a;
    --lime: #8ebe3f;
    --icon-green: #7fb83a;
  }
  * { box-sizing: border-box; margin: 0; padding: 0; }
  html, body {
    width: 1200px;
    height: 900px;
    overflow: hidden;
    background: var(--page-bg);
    font-family: "Poppins", sans-serif;
  }
  .canvas {
    width: 1200px;
    height: 900px;
    display: flex;
    align-items: center;
    justify-content: center;
  }
  .business-card {
    position: relative;
    width: 980px;
    height: 560px;
    background: var(--card-bg);
    box-shadow: 0 20px 50px rgba(0,0,0,0.5);
  }
  .brand-mark {
    position: absolute;
    left: 90px;
    top: 110px;
    width: 300px;
    height: 300px;
    background: var(--forest);
  }
  .company {
    position: absolute;
    left: 500px;
    top: 150px;
    color: var(--ink);
  }
  .company-name {
    font-size: 54px;
    font-weight: 600;
    line-height: 1;
    letter-spacing: 0.5px;
  }
  .company-suffix {
    font-size: 54px;
    font-weight: 600;
    line-height: 1.1;
  }
  .contact {
    position: absolute;
    left: 500px;
    top: 340px;
    color: var(--ink);
  }
  .person-name {
    font-size: 30px;
    font-weight: 700;
    line-height: 1.1;
  }
  .person-title {
    font-size: 20px;
    font-weight: 400;
    color: var(--forest);
    margin-bottom: 14px;
  }
  .contact-list { list-style: none; }
  .contact-item {
    display: flex;
    align-items: center;
    gap: 12px;
    font-size: 20px;
    line-height: 1.45;
  }
  .contact-icon { width: 20px; height: 20px; flex: none; }
</style>
</head>
<body>
<main class="canvas">
  <section class="business-card">
    <div class="brand-mark" aria-hidden="true"></div>

    <div class="company">
      <p class="company-name">Verdant Cover</p>
      <p class="company-suffix">Pty Ltd</p>
    </div>

    <div class="contact">
      <p class="person-name">Marcus Delaney</p>
      <p class="person-title">Managing Director</p>
      <ul class="contact-list">
        <li class="contact-item">
          <svg class="contact-icon" viewBox="0 0 24 24" aria-label="Office phone">
            <path fill="var(--icon-green)" d="M6.6 10.8a15.1 15.1 0 0 0 6.6 6.6l2.2-2.2c.3-.3.7-.4 1-.2 1.1.4 2.3.6 3.6.6.6 0 1 .4 1 1V20c0 .6-.4 1-1 1A17 17 0 0 1 3 4c0-.6.4-1 1-1h3.5c.6 0 1 .4 1 1 0 1.3.2 2.5.6 3.6.1.3 0 .7-.2 1z"/>
          </svg>
          214-555-0186
        </li>
        <li class="contact-item">
          <svg class="contact-icon" viewBox="0 0 24 24" aria-label="Mobile phone">
            <rect x="6" y="2" width="12" height="20" rx="2" fill="none" stroke="var(--icon-green)" stroke-width="2"/>
            <circle cx="12" cy="18" r="1.2" fill="var(--icon-green)"/>
          </svg>
          214-555-0137
        </li>
        <li class="contact-item">
          <svg class="contact-icon" viewBox="0 0 24 24" aria-label="Email">
            <rect x="2" y="5" width="20" height="14" fill="var(--icon-green)"/>
            <path d="M2 5l10 8 10-8M2 19l7-7M22 19l-7-7" fill="none" stroke="#fff" stroke-width="1.5"/>
          </svg>
          marcus@verdantcover.com
        </li>
      </ul>
    </div>
  </section>
</main>
</body>
</html>
```